Mailer Ad for Private Gym

We need a clean and modern front and back mailer for our upscale, modern gym. Must follow project brief and be cohesive with our current brand. We have uploaded the layout sketch in the brief as well. Please refer to our website corevaultfitness.example for additional branding, logo, and gym info.

Target Market(s)

high-end upscale market

Industry/Entity Type

Gym

Font styles to use
Sans Serif

Colors
ec1f27
ffffff

Requirements
Must have
• *** EXACT LAYOUT OF FRONT AND BACK OF POST CARD ATTACHED TO BRIEF.
• Please include:
• FRONT:
• Icons attached from our website: Weight loss, Build Strength, etc
• THE OFFER: "20% Off 2 Weeks of Personal Training*
• *Please see see back for details"
• BOTTOM COPY: Adjacent to Harlow College on Pell Avenue
• BACK SIDE:
• Attached shot of Gym
• ITALICS: *To redeem this offer, email us at contact@corevaultfitness.example with the subject line "Around the Corner". Offer is good for 20% off 2 weeks of personal training. The minimum amount of sessions is 2 per week. Offer good until 11.30.16
• (final design will also need expiration dates of 1/31/17 2/28/17 and 3/31/17)
• ~ Phone, Address, website at the bottom:
• 482 Pell Avenue, Durham, NC
• contact@corevaultfitness.example
• corevaultfitness.example
• 919.555.0274
• ~ Leave the right left blank for the address
• MUST BE clean, so it is easy to read.
• Stick to white postcard with grey, black, bright red/orange like website and logo
Should not have
• Crowded, messy, design.

```html
<!DOCTYPE html>
<html lang="en">
<head>
<meta charset="utf-8">
<title>Core Vault Mailer Front</title>
<link rel="stylesheet" href="https://fonts.googleapis.com/css2?family=Arimo:wght@400;700&family=Cabin:wght@600&family=Mulish:ital,wght@0,700;0,800;1,600&display=swap">
<style>
  :root {
    --brand-red: #ec3a24;
    --ink: #4a4a4c;
    --band: #58595b;
    --paper: #ffffff;
    --photo-light: #f1f1f1;
    --photo-mid: #dcdcdc;
  }
  * { margin: 0; padding: 0; box-sizing: border-box; }
  html, body { width: 1200px; height: 776px; overflow: hidden; background: var(--paper); }
  .mailer { position: relative; width: 1200px; height: 776px; background: var(--paper); }
  .gym-photo {
    position: absolute; left: 18px; top: 18px; width: 1164px; height: 740px;
    background: radial-gradient(ellipse at 75% 45%, var(--photo-mid), var(--photo-light) 65%);
  }
  .brand {
    position: absolute; left: 38px; top: 86px; width: 356px;
    display: flex; align-items: center; gap: 12px;
  }
  .brand-mark { width: 26px; height: 26px; background: var(--brand-red); flex: none; }
  .brand-name {
    font-family: "Mulish", sans-serif; font-weight: 800; font-size: 50px;
    color: var(--ink); letter-spacing: 1px; line-height: 1;
  }
  .brand-tag {
    position: absolute; left: 44px; top: 182px;
    font-family: "Mulish", sans-serif; font-weight: 800; font-size: 13px;
    letter-spacing: 6.3px; color: var(--ink);
  }
  .offer {
    position: absolute; left: 415px; top: 70px; width: 369px; height: 147px;
    background: var(--brand-red); color: var(--paper); text-align: center;
    font-family: "Arimo", sans-serif;
  }
  .offer::after {
    content: ""; position: absolute; inset: 8px; border: 1px dotted rgba(255,255,255,.55);
  }
  .offer-title { margin-top: 21px; font-weight: 700; font-size: 17px; }
  .offer-deal { margin-top: 2px; font-weight: 700; font-size: 53px; line-height: 1.1; }
  .offer-deal small { font-size: 20px; vertical-align: 20px; margin-right: 4px; }
  .offer-note { font-size: 17px; margin-top: 2px; }
  .award { position: absolute; left: 880px; top: 32px; width: 224px; height: 224px; border-radius: 50%; background: var(--brand-red); }
  .headline {
    position: absolute; left: 0; width: 1200px; top: 312px; text-align: center;
    font-family: "Mulish", sans-serif; font-weight: 800; font-size: 57px; color: var(--ink);
    letter-spacing: 1px;
  }
  .benefits { position: absolute; top: 420px; left: 0; width: 1200px; }
  .benefit { position: absolute; width: 320px; text-align: center; }
  .benefit svg { display: block; margin: 0 auto; height: 76px; }
  .benefit-label {
    margin-top: 38px; font-family: "Mulish", sans-serif; font-weight: 800;
    font-size: 29px; color: var(--ink);
  }
  .location-band {
    position: absolute; left: 18px; top: 614px; width: 1164px; height: 67px;
    background: var(--band); color: var(--paper); text-align: center;
    font-family: "Cabin", sans-serif; font-weight: 600; font-size: 36px; line-height: 67px;
    letter-spacing: .5px;
  }
  .location-note {
    position: absolute; left: 0; width: 1200px; top: 706px; text-align: center;
    font-family: "Mulish", sans-serif; font-style: italic; font-weight: 600;
    font-size: 22px; color: var(--ink); letter-spacing: .5px;
  }
</style>
</head>
<body>
<main class="mailer">
  <div class="gym-photo" role="img" aria-label="Faded gym photo of gloved hands gripping a barbell"></div>

  <div class="brand">
    <span class="brand-mark"></span>
    <span class="brand-name">CORE VAULT</span>
  </div>
  <div class="brand-tag">PERSONAL TRAINING STUDIO</div>

  <section class="offer">
    <p class="offer-title">2 WEEKS OF PERSONAL TRAINING</p>
    <p class="offer-deal"><small>Get</small>20% OFF</p>
    <p class="offer-note">(Please see see back for details)</p>
  </section>

  <div class="award" role="img" aria-label="Local award badge"></div>

  <h1 class="headline">What can Core Vault do for you?</h1>

  <section class="benefits">
    <div class="benefit" style="left:74px">
      <svg viewBox="0 0 70 76" aria-hidden="true">
        <path d="M14 14 Q35 0 56 14 L66 42 Q70 72 40 72 L30 72 Q0 72 4 42 Z" fill="var(--brand-red)"/>
        <circle cx="35" cy="26" r="13" fill="#fff"/>
        <circle cx="35" cy="26" r="9" fill="var(--brand-red)"/>
        <line x1="35" y1="26" x2="41" y2="20" stroke="#fff" stroke-width="3"/>
        <line x1="35" y1="42" x2="35" y2="60" stroke="#fff" stroke-width="2"/>
      </svg>
      <p class="benefit-label">Weight Loss</p>
    </div>
    <div class="benefit" style="left:429px">
      <svg viewBox="0 0 76 76" aria-hidden="true" fill="var(--brand-red)">
        <rect x="0" y="32" width="5" height="12" rx="2"/>
        <rect x="8" y="20" width="9" height="36" rx="3"/>
        <rect x="20" y="12" width="9" height="52" rx="3"/>
        <rect x="29" y="35" width="18" height="6"/>
        <rect x="47" y="12" width="9" height="52" rx="3"/>
        <rect x="59" y="20" width="9" height="36" rx="3"/>
        <rect x="71" y="32" width="5" height="12" rx="2"/>
      </svg>
      <p class="benefit-label">Build Strength</p>
    </div>
    <div class="benefit" style="left:781px">
      <svg viewBox="0 0 90 76" aria-hidden="true">
        <circle cx="10" cy="24" r="7" fill="var(--brand-red)"/>
        <path d="M18 28 L40 36 L56 8" stroke="var(--brand-red)" stroke-width="8" fill="none" stroke-linecap="round" stroke-linejoin="round"/>
        <path d="M48 22 L40 36 L30 70 M40 36 L54 48 L68 72" stroke="var(--brand-red)" stroke-width="8" fill="none" stroke-linecap="round" stroke-linejoin="round"/>
      </svg>
      <p class="benefit-label">Increase Flexibility</p>
    </div>
  </section>

  <div class="location-band">RIGHT ACROSS FROM THE HARLOW WALL ON PELL AVENUE</div>
  <p class="location-note">Adjacent to Harlow College on Pell Avenue</p>
</main>
</body>
</html>
```